Velto Business Card

1. We need a double sided business card ready to print by Wed 26 June.
2. Our business name is Velto
3. We trade under the name Velto Consult.
4. The card will be printed by Pib or CardNorra on a 85mmx55mm card with rounded edges (standard size). The card will be on a luxury finish and we dont mind the logo or contact details being embossed in silver or a suitable colour.
5. The card should be simple and classy representing a management consultancy. Slimmer and large fonts should be used
6. Our website is www.veltoconsult.example
7. We dont want a tag line
8. The cards are for three partners, therefore the same design will be used to add details for each of the 3 partners, therefore the files we receive should be editable.
9. The contact details to include as a minimum:
Name First Name Last Name
Position: Partner
Telephone +44 7612 555 123
email: first.last@veltoconsult.example
10. This is our linkedIn Page: https://www.linkedin.example/company/velto-group/ to get an idea of our business (do not use on the card)
11. We want one side to have the logo in the middle, could be silver and embossed with a single dark blue colour in the background.
12. Our accent (>) and contact details should be on the reverse side with a white background, perhaps replace the website with QR code.
13. The text should be legible and large and look classy and professional, maybe slimmer fonts
14. You do not need to keep to the colours we have provided, be creative
15. We want the original files, vectors, jpeg, .ai and .png files ready to print.
16. We want the options to make several revisions to get the card right.

```html
<!DOCTYPE html>
<html lang="en">
<head>
<meta charset="utf-8">
<title>Velto Business Card</title>
<link rel="stylesheet" href="https://fonts.googleapis.com/css2?family=Lato:wght@400;700;900&display=swap">
<style>
  :root {
    --stage: #2a2a2c;
    --navy: #020a38;
    --white: #ffffff;
    --silver: #e9e9ec;
    --gold: #fdb913;
    --orange: #f7941d;
    --ink: #222222;
  }
  * { box-sizing: border-box; margin: 0; padding: 0; }
  html, body {
    width: 1200px; height: 982px; overflow: hidden;
    background: var(--stage);
    font-family: "Lato", sans-serif;
  }
  .stage {
    width: 1200px; height: 982px;
    display: flex; flex-direction: column;
    align-items: center; justify-content: center; gap: 44px;
  }
  .card {
    position: relative;
    width: 660px; height: 427px;
    border-radius: 26px;
    overflow: hidden;
  }
  .card--front {
    background: var(--navy);
    display: flex; align-items: center; justify-content: center;
  }
  .card--back { background: var(--white); }

  .wordmark {
    display: flex; align-items: flex-start; gap: 10px;
    font-weight: 900; letter-spacing: -4px; line-height: 1;
  }
  .wordmark__mark {
    width: 18px; height: 18px; margin-top: 22px;
    background: var(--orange);
  }
  .card--front .wordmark { font-size: 132px; color: var(--silver); }
  .card--back .wordmark {
    position: absolute; top: 78px; left: 0; right: 0;
    justify-content: center;
    font-size: 118px; color: var(--navy);
  }

  .holder {
    position: absolute; top: 262px; right: 345px;
    text-align: right;
  }
  .holder__name {
    font-weight: 900; font-size: 31px; color: var(--navy);
    letter-spacing: 0.5px; text-transform: uppercase;
  }
  .holder__role {
    font-weight: 400; font-size: 24px; color: var(--gold);
    margin-top: 4px;
  }
  .divider {
    position: absolute; left: 335px; top: 256px;
    width: 2px; height: 96px; background: var(--navy);
  }
  .contacts {
    position: absolute; left: 358px; top: 262px;
    list-style: none;
    display: flex; flex-direction: column; gap: 8px;
  }
  .contacts__item {
    display: flex; align-items: center; gap: 12px;
    font-size: 20px; color: var(--ink);
  }
  .contacts__icon { width: 18px; height: 18px; flex: none; }
</style>
</head>
<body>
<main class="stage">
  <section class="card card--front" aria-label="Front of card">
    <div class="wordmark"><span>velto</span><span class="wordmark__mark"></span></div>
  </section>

  <section class="card card--back" aria-label="Back of card">
    <div class="wordmark"><span>velto</span><span class="wordmark__mark"></span></div>

    <div class="holder">
      <p class="holder__name">Daniel Hart</p>
      <p class="holder__role">Founder &amp; CEO</p>
    </div>

    <div class="divider"></div>

    <ul class="contacts">
      <li class="contacts__item">
        <svg class="contacts__icon" viewBox="0 0 24 24" aria-hidden="true">
          <path fill="var(--orange)" d="M6.6 10.8a15.1 15.1 0 0 0 6.6 6.6l2.2-2.2a1 1 0 0 1 1-.25 11.4 11.4 0 0 0 3.6.57 1 1 0 0 1 1 1V20a1 1 0 0 1-1 1A17 17 0 0 1 3 4a1 1 0 0 1 1-1h3.5a1 1 0 0 1 1 1c0 1.25.2 2.45.57 3.57a1 1 0 0 1-.25 1z"/>
        </svg>
        <span>+44 7612 555 123</span>
      </li>
      <li class="contacts__item">
        <svg class="contacts__icon" viewBox="0 0 24 24" aria-hidden="true">
          <rect x="2" y="5" width="20" height="14" rx="1.5" fill="var(--orange)"/>
          <path d="M3 6.5l9 6.5 9-6.5" fill="none" stroke="var(--white)" stroke-width="1.6"/>
        </svg>
        <span>dhart@veltoconsult.example</span>
      </li>
      <li class="contacts__item">
        <svg class="contacts__icon" viewBox="0 0 24 24" aria-hidden="true">
          <circle cx="12" cy="12" r="9.5" fill="none" stroke="var(--orange)" stroke-width="2"/>
          <ellipse cx="12" cy="12" rx="4" ry="9.5" fill="none" stroke="var(--orange)" stroke-width="1.6"/>
          <path d="M2.5 12h19" stroke="var(--orange)" stroke-width="1.6"/>
        </svg>
        <span>veltoconsult.example</span>
      </li>
    </ul>
  </section>
</main>
</body>
</html>
```